Email Signature

We want a new email signature designed that will include an employees picture and our logo at minimum. Of course contact info as well.

For the sample please create the new signature for Dale Prewitt...extra pics provided
please visit our website www.BrightwayUpkeep.com

Need to limit links to our website....government email servers strip out many.
Updates

I have a new draft design I'd like to work from...simple and clean.Needs:LogoDisclaimerand a bit of colorI'd like to make selection this week. Added Tuesday, October 24, 2017

Target Market(s)

other professional businesses

Requirements
Must have
• picture & Logo
• new look and something that auto scales to the emails window.
• Would like to have a new tag line "

```html
<!DOCTYPE html>
<html lang="en">
<head>
<meta charset="utf-8">
<title>Email Signature – Dale Prewitt</title>
<link rel="stylesheet" href="https://fonts.googleapis.com/css2?family=Lato:wght@400;700&family=Yellowtail&display=swap">
<style>
  :root {
    --page-bg: #c7c7c7;
    --sheet: #ffffff;
    --ink: #111111;
    --brand-blue: #2d3e9e;
    --accent-red: #e0302a;
    --rule: #9a9a9a;
    --legal: #555555;
  }
  * { margin: 0; padding: 0; box-sizing: border-box; }
  html, body { width: 1200px; height: 1000px; overflow: hidden; }
  body {
    background: var(--page-bg);
    font-family: "Lato", Arial, sans-serif;
    color: var(--ink);
    position: relative;
  }
  .signature {
    position: absolute;
    left: 214px; top: 367px;
    width: 816px; height: 328px;
    background: var(--sheet);
  }
  .sign-off {
    position: absolute; left: 35px; top: 17px;
    font-size: 12px; font-weight: 700;
  }
  .person-name {
    position: absolute; left: 35px; top: 52px;
    font-family: "Yellowtail", cursive;
    font-size: 21px; color: var(--brand-blue);
    line-height: 1;
  }
  .job-title {
    position: absolute; left: 154px; top: 60px;
    font-size: 13px;
  }
  .portrait {
    position: absolute; left: 34px; top: 85px;
    width: 82px; height: 82px;
  }
  .contact-list {
    position: absolute; left: 151px; top: 86px;
    list-style: none; font-size: 13px; line-height: 16px;
  }
  .contact-list .label {
    color: var(--brand-blue);
    display: inline-block; width: 22px;
  }
  .company-mark {
    position: absolute; left: 34px; top: 190px;
    width: 104px;
    font-size: 14px; font-weight: 700; line-height: 1.05;
    color: var(--accent-red); text-align: center;
  }
  .address {
    position: absolute; left: 151px; top: 183px;
    font-size: 13px;
  }
  .services {
    position: absolute; left: 151px; top: 199px;
    font-size: 13px; line-height: 16px; color: var(--brand-blue);
  }
  .services .sep { color: var(--ink); margin: 0 5px; }
  .divider {
    position: absolute; left: 35px; top: 247px;
    width: 776px; height: 1px; background: var(--rule);
  }
  .disclaimer {
    position: absolute; left: 35px; top: 262px;
    width: 778px;
    font-size: 8.3px; line-height: 10px; color: var(--legal);
    font-weight: 700;
  }
</style>
</head>
<body>
  <section class="signature">
    <p class="sign-off">Thank you,</p>
    <p class="person-name">Dale Prewitt</p>
    <p class="job-title">Director of Pre-Construction</p>

    <svg class="portrait" viewBox="0 0 82 82" role="img" aria-label="Portrait photo of Dale Prewitt">
      <defs>
        <linearGradient id="portrait-tone" x1="0" y1="0" x2="0" y2="1">
          <stop offset="0" stop-color="#d9d4cf"/>
          <stop offset="1" stop-color="#3a3940"/>
        </linearGradient>
      </defs>
      <circle cx="41" cy="41" r="39.5" fill="url(#portrait-tone)" stroke="#e0302a" stroke-width="2"/>
    </svg>

    <ul class="contact-list">
      <li><span class="label">C.</span>410-555-0148</li>
      <li><span class="label">O.</span>800-555-0192 x206</li>
      <li><span class="label">F.</span>800-555-0193</li>
      <li><span class="label">E.</span>DPrewitt@BrightwayUpkeep.com</li>
      <li><span class="label">W.</span>www.BrightwayUpkeep.com</li>
    </ul>

    <p class="company-mark">Brightway Upkeep</p>

    <p class="address">415 Harbor Ridge Road Suite B, Glen Burnie, Maryland 21061</p>
    <p class="services">
      Electrical<span class="sep">|</span>Roadway<span class="sep">|</span>Athletic Field<span class="sep">|</span>Utility<span class="sep">|</span>Energy Audits<span class="sep">|</span>Banners<span class="sep">|</span>Directional Drilling<span class="sep">|</span>Night Inspections<br>
      Pole Safety<span class="sep">|</span>Interior Lighting<span class="sep">|</span>Signs<span class="sep">|</span>Street Lighting<span class="sep">|</span>Traffic Signals<span class="sep">|</span>Lighting Upgrades<span class="sep">|</span>Employment
    </p>

    <div class="divider"></div>

    <p class="disclaimer">This Email message and any attachment may contain information that is proprietary, legally privileged, confidential, and/or subject to copyright belonging to Brightway Upkeep Inc ("BUI"). This Email is intended solely for the use of the person(s) to which it is addressed and is not subject to FOIA. If you are not an intended recipient, or the employee or agent responsible for delivery of this Email to the intended recipient(s), you are hereby notified that any dissemination, distribution or copying of this Email is strictly prohibited. If you have received this message in error, please immediately notify the sender and permanently delete this Email and any copies. BUI policies expressly prohibit employees from making defamatory or offensive statements and infringing any copyright or any other legal right by Email communication. BUI will not accept any liability in respect of such communications</p>
  </section>
</body>
</html>
```